Brivomark Business Card

Brivomark is a young and energetic software development consultancy. We spend our time on the road working with clients on their sites an meeting new potential customers and employees!

We need a sharp, vibrant and memorable business card that will inspires those that receive it to look after it as it oozes quality and is a nice thing in its own right.

We like bold colours and distinctive design. So show us what you can do.

In terms of information on the card, it would be good to see:

* Our logo (Obviously :) )
* Employee name
* Email
* Website address
* Mobile number
* Full company name (Brivomark ltd)
* Registered company number
* Registered company address

Industry/Entity Type

Software

Requirements
Nice to have
• We are thinking that having a QR Code on the business card could be a good way of adding active marketing. It would be good to see if you are able to merge the kind of element in to your designs!

Maybe something special could be achieved using a visual QR Code like those produced at http://www.quenprint-example.com/ ? You have our media so feel free to have a play.

```html
<!DOCTYPE html>
<html lang="en">
<head>
<meta charset="utf-8">
<title>Brivomark Business Card</title>
<link href="https://fonts.googleapis.com/css2?family=Open+Sans:wght@400;600;700&display=swap" rel="stylesheet">
<style>
  :root {
    --brand-red: #c8202f;
    --ink: #4a4a4a;
    --ink-dark: #333333;
    --card: #ffffff;
    --backdrop: #ece9e4;
    --divider: #cfcfcf;
  }
  * { margin: 0; padding: 0; box-sizing: border-box; }
  html, body {
    width: 1200px; height: 720px; overflow: hidden;
    background: var(--backdrop);
    font-family: "Open Sans", Arial, sans-serif;
  }
  .canvas {
    position: relative; width: 1200px; height: 720px;
    display: flex; align-items: center; justify-content: center; gap: 40px;
  }
  .card {
    position: relative; width: 540px; height: 309px;
    background: var(--card);
    box-shadow: 0 2px 10px rgba(0,0,0,0.12);
  }
  .wordmark {
    color: var(--brand-red);
    font-weight: 400;
    letter-spacing: 1px;
    line-height: 1;
    white-space: nowrap;
  }
  /* Front: contact side */
  .card--front .wordmark {
    position: absolute; top: 58px; left: 0; right: 0;
    text-align: center; font-size: 62px;
  }
  .identity {
    position: absolute; top: 172px; right: 288px;
    text-align: right; color: var(--ink); font-size: 14px; line-height: 1.3;
  }
  .identity__name { color: var(--brand-red); font-weight: 700; font-size: 17px; }
  .divider {
    position: absolute; top: 160px; left: 266px;
    width: 1px; height: 110px; background: var(--divider);
  }
  .contacts {
    position: absolute; top: 160px; left: 280px;
    list-style: none; color: var(--ink); font-size: 14px;
  }
  .contacts li { display: flex; align-items: center; gap: 8px; height: 22px; }
  .contacts svg { width: 14px; height: 14px; flex: none; }
  /* Back: brand side */
  .card--back .wordmark {
    position: absolute; top: 112px; left: 0; right: 0;
    text-align: center; font-size: 66px;
  }
  .web-address {
    position: absolute; bottom: 34px; left: 0; right: 0;
    text-align: center; font-size: 15px; font-weight: 700;
    letter-spacing: 1.5px; color: var(--ink-dark);
  }
  .web-address__name { color: var(--brand-red); }
</style>
</head>
<body>
<main class="canvas">
  <section class="card card--front" aria-label="Business card, contact side">
    <div class="wordmark">BRIVOMARK</div>
    <div class="identity">
      <div class="identity__name">Your Name</div>
      <div class="identity__title">Title</div>
      <div>00, Complex Name</div>
      <div>City, State 004</div>
    </div>
    <div class="divider"></div>
    <ul class="contacts">
      <li>
        <svg viewBox="0 0 14 14" aria-hidden="true"><circle cx="7" cy="7" r="7" fill="var(--brand-red)"/><path d="M4.5 3.5 L6 3.5 L6.5 5.5 L5.6 6.2 Q6.5 8 7.8 8.6 L8.5 7.7 L10.5 8.2 L10.5 9.7 Q7 10.5 4.3 6.5 Q3.8 4.5 4.5 3.5Z" fill="#fff"/></svg>
        123-456-7890
      </li>
      <li>
        <svg viewBox="0 0 14 14" aria-hidden="true"><circle cx="7" cy="7" r="7" fill="var(--brand-red)"/><rect x="4.8" y="3" width="4.4" height="8" rx="0.8" fill="#fff"/><rect x="5.5" y="4" width="3" height="4.4" fill="var(--brand-red)"/></svg>
        123-456-7890
      </li>
      <li>
        <svg viewBox="0 0 14 14" aria-hidden="true"><circle cx="7" cy="7" r="7" fill="var(--brand-red)"/><rect x="3.5" y="4.5" width="7" height="5" fill="#fff"/><path d="M3.5 4.5 L7 7.3 L10.5 4.5" fill="none" stroke="var(--brand-red)" stroke-width="0.8"/></svg>
        info@brivomark.com
      </li>
      <li>
        <svg viewBox="0 0 14 14" aria-hidden="true"><circle cx="7" cy="7" r="7" fill="var(--brand-red)"/><g fill="none" stroke="#fff" stroke-width="0.9"><circle cx="7" cy="7" r="3.8"/><ellipse cx="7" cy="7" rx="1.6" ry="3.8"/><line x1="3.2" y1="7" x2="10.8" y2="7"/></g></svg>
        www.brivomark.com
      </li>
    </ul>
  </section>

  <section class="card card--back" aria-label="Business card, brand side">
    <div class="wordmark">BRIVOMARK</div>
    <div class="web-address">www.<span class="web-address__name">brivomark</span>.com</div>
  </section>
</main>
</body>
</html>
```